Label designs for three different cider varieties

The Hollin Perry Works is a family run business. We have been making cider within the family as a hobby for over 100 years and we have recently decided to start to try to sell the cider. Therefore this project is to create a logo and three product labels for three different varieties of cider. So we should end up with four files; one for the logo and one for each of the labels. The files need to be in an editable format for us so that we can add edit the batch numbers e.g. PNG file.
For the logo we would like to use the Lark Family Shield since Lark is our family name. We would like it adapted into a cider themed crest, for example with apples and trees. We are open to ideas about the logo but this is just our initial idea. Example of the original Lark Family Shield can be seen in the link below:
http://www.plumevault.net/coats/Lark-England.jpg
The labels should be no bigger than 93mm in height and 213mm in length. Each label should be similar in style so it is clear the three different varieties of cider are from the same company. Each label must have the following information since this is a legal requirement:
- The logo you have created
- The Hollin Perry Works Ltd.
- 42 Milford Terrace, Taunton, Somerset, TA4 9QJ
- Alcohol: 6% vol
- 500ml
- Allergens: Contains Sulphites for freshness
- There needs to be space on the label for batch numbers. This is four numbers e.g. 1701.
- Family craft cider makers using only premium apples from our own traditional Somerset orchard.
The names of the three cider varieties are:
- Hollin Traditional
- Hollin Golden
- Hollin Quarrow
Our initial idea is that each variety would have its own colour associated with it; i.e. black themed label for Hollin Traditional, gold themed label for Hollin Golden and a red themed label for Hollin Quarrow. The crest logo you have created would then be in the themed colour for that cider variety i.e. black, gold or red.
We would like the labels to reflect the following themes for our brand:
- High end premium brand
- Clean and simple design
- Modern
Overall we are very open to ideas and we do not want to constrain your creativity. All of the above is just our initial ideas but we would love to see what ideas you have. The only things that cannot change are what must be on the label since this is a legal requirement we have to meet.

```html
<!DOCTYPE html>
<html lang="en">
<head>
<meta charset="utf-8">
<title>Hollin Cyder — Label Set</title>
<link rel="stylesheet" href="https://fonts.googleapis.com/css2?family=EB+Garamond:wght@400;500&family=Playfair+Display:wght@900&display=swap">
<style>
  :root {
    --canvas: #ffffff;
    --label-dark: #121212;
    --label-mid: #2c2c2c;
    --frame-line: rgba(255, 255, 255, 0.18);
    --ink: #ffffff;
    --ink-soft: #e8e8e8;
    --batch-box: #ffffff;
    --batch-ink: #1a1a1a;
    --silver: #c9c9c9;
    --traditional: #9cc21f;
    --golden: #d4a320;
    --quarrow: #e3161e;
  }
  html, body {
    margin: 0;
    padding: 0;
    width: 1200px;
    height: 1200px;
    overflow: hidden;
    background: var(--canvas);
  }
  .sheet {
    position: relative;
    width: 1200px;
    height: 1200px;
  }
  .label {
    position: absolute;
    width: 304px;
    height: 494px;
    background:
      linear-gradient(125deg, transparent 30%, rgba(255,255,255,0.07) 48%, transparent 66%),
      linear-gradient(180deg, var(--label-mid), var(--label-dark));
    color: var(--ink);
    font-family: "EB Garamond", Georgia, serif;
    text-align: center;
    box-sizing: border-box;
  }
  .label::after {
    content: "";
    position: absolute;
    inset: 8px;
    border: 1px solid var(--frame-line);
    pointer-events: none;
  }
  .label--traditional { --theme: var(--traditional); }
  .label--golden { --theme: var(--golden); }
  .label--quarrow { --theme: var(--quarrow); }

  .col-1 { left: 114px; }
  .col-2 { left: 447px; }
  .col-3 { left: 780px; }
  .row-front { top: 50px; }
  .row-back { top: 606px; }

  .label > * { position: absolute; left: 0; right: 0; margin: 0; }

  .house { font-family: "Playfair Display", Georgia, serif; font-weight: 900; letter-spacing: 0.06em; line-height: 1; }
  .variety { font-family: "Playfair Display", Georgia, serif; font-weight: 900; letter-spacing: -0.02em; text-transform: uppercase; line-height: 1; }
  .style-note { line-height: 1; }
  .motif {
    left: 50%;
    border-radius: 3px;
    background: var(--theme);
    opacity: 0.9;
  }
  .crest-art {
    left: 50%;
    border-radius: 46% 46% 40% 40%;
    background: radial-gradient(ellipse at 50% 45%, var(--silver) 0 28%, color-mix(in srgb, var(--theme) 85%, #000) 52%, transparent 72%);
  }
  .brand-name { letter-spacing: 0.02em; text-transform: uppercase; font-weight: 500; line-height: 1; }

  /* front */
  .label--front .motif { top: 18px; width: 48px; height: 38px; margin-left: -24px; }
  .label--front .house { top: 74px; font-size: 9px; }
  .label--front .variety { top: 88px; font-size: 30px; }
  .label--front .style-note { top: 140px; font-size: 17px; }
  .label--front .crest-art { top: 186px; width: 280px; height: 200px; margin-left: -140px; }
  .label--front .brand-name { top: 402px; font-size: 22px; }
  .label--front .strength { top: 440px; font-size: 18px; line-height: 1; }
  .label--front .volume { top: 457px; font-size: 18px; line-height: 1; }

  /* back */
  .label--back .house { top: 56px; font-size: 6px; }
  .label--back .variety { top: 64px; font-size: 18px; }
  .label--back .style-note { top: 90px; font-size: 10px; }
  .label--back .crest-art { top: 112px; width: 170px; height: 130px; margin-left: -85px; }
  .label--back .brand-name { top: 251px; font-size: 13px; }
  .label--back .story { top: 326px; font-size: 15px; line-height: 1.0; }
  .label--back .allergens { top: 380px; font-size: 11px; }
  .label--back .batch {
    top: 402px; left: 72px; right: 72px; height: 28px;
    background: var(--batch-box); color: var(--batch-ink);
    font-size: 11.5px; line-height: 28px; letter-spacing: 0.02em;
  }
  .label--back .maker { top: 440px; font-size: 11px; line-height: 1.25; color: var(--ink-soft); }
</style>
</head>
<body>
<main class="sheet">

  <section class="label label--front label--traditional col-1 row-front">
    <div class="motif" role="img" aria-label="Small barrel motif in the variety colour"></div>
    <p class="house">HOLLIN</p>
    <h2 class="variety">Traditional</h2>
    <p class="style-note">Dry Cyder</p>
    <div class="crest-art" role="img" aria-label="Hollin Cyder emblem artwork in green"></div>
    <p class="brand-name">Hollin Cyder</p>
    <p class="strength">ALC: 6% vol</p>
    <p class="volume">500ml</p>
  </section>

  <section class="label label--front label--golden col-2 row-front">
    <div class="motif" role="img" aria-label="Small barrel motif in the variety colour"></div>
    <p class="house">HOLLIN</p>
    <h2 class="variety">Golden</h2>
    <p class="style-note">Medium Dry<br>Cyder</p>
    <div class="crest-art" role="img" aria-label="Hollin Cyder emblem artwork in gold"></div>
    <p class="brand-name">Hollin Cyder</p>
    <p class="strength">ALC: 6% vol</p>
    <p class="volume">500ml</p>
  </section>

  <section class="label label--front label--quarrow col-3 row-front">
    <div class="motif" role="img" aria-label="Small barrel motif in the variety colour"></div>
    <p class="house">HOLLIN</p>
    <h2 class="variety">Quarrow</h2>
    <p class="style-note">Single Variety<br>Cyder</p>
    <div class="crest-art" role="img" aria-label="Hollin Cyder emblem artwork in red"></div>
    <p class="brand-name">Hollin Cyder</p>
    <p class="strength">ALC: 6% vol</p>
    <p class="volume">500ml</p>
  </section>

  <section class="label label--back label--traditional col-1 row-back">
    <p class="house">HOLLIN</p>
    <h2 class="variety">Traditional</h2>
    <p class="style-note">Dry Cyder</p>
    <div class="crest-art" role="img" aria-label="Hollin Cyder emblem artwork in green"></div>
    <p class="brand-name">Hollin Cyder</p>
    <p class="story">Family craft cider makers using only<br>premium apples from our own<br>traditional Somerset orchard.</p>
    <p class="allergens">Allergens: Contains Sulphites for freshness</p>
    <p class="batch">BATCH NUMBERS</p>
    <p class="maker">The Hollin Perry Works Ltd.<br>42 Milford Terrace, Taunton, Somerset, TA4 9QJ</p>
  </section>

  <section class="label label--back label--golden col-2 row-back">
    <p class="house">HOLLIN</p>
    <h2 class="variety">Golden</h2>
    <p class="style-note">Medium Dry<br>Cyder</p>
    <div class="crest-art" role="img" aria-label="Hollin Cyder emblem artwork in gold"></div>
    <p class="brand-name">Hollin Cyder</p>
    <p class="story">Family craft cider makers using only<br>premium apples from our own<br>traditional Somerset orchard.</p>
    <p class="allergens">Allergens: Contains Sulphites for freshness</p>
    <p class="batch">BATCH NUMBERS</p>
    <p class="maker">The Hollin Perry Works Ltd.<br>42 Milford Terrace, Taunton, Somerset, TA4 9QJ</p>
  </section>

  <section class="label label--back label--quarrow col-3 row-back">
    <p class="house">HOLLIN</p>
    <h2 class="variety">Quarrow</h2>
    <p class="style-note">Single Variety<br>Cyder</p>
    <div class="crest-art" role="img" aria-label="Hollin Cyder emblem artwork in red"></div>
    <p class="brand-name">Hollin Cyder</p>
    <p class="story">Family craft cider makers using only<br>premium apples from our own<br>traditional Somerset orchard.</p>
    <p class="allergens">Allergens: Contains Sulphites for freshness</p>
    <p class="batch">BATCH NUMBERS</p>
    <p class="maker">The Hollin Perry Works Ltd.<br>42 Milford Terrace, Taunton, Somerset, TA4 9QJ</p>
  </section>

</main>
</body>
</html>
```